Brookfell Self Storage - Business Sign

The sign we are needing designed is our main road sign for our self-storage business. The dimensions of the sign are 57 inches tall x 96 inches wide. We require that our attached logo be on the sign as well as our phone number: 478-216-4387 and website www.BrookfellStorage.net. Optional information that can be added but not required is our address: 418 Marlow Tenney Pkwy, Centerville, GA 31047.

Industry/Entity Type

Self Storage

Font styles to use
Sans Serif

```html
<!DOCTYPE html>
<html lang="en">
<head>
<meta charset="utf-8">
<title>Brookfell Self Storage – Road Sign</title>
<link rel="stylesheet" href="https://fonts.googleapis.com/css2?family=Montserrat:wght@700&family=Open+Sans:wght@400&display=swap">
<style>
  :root {
    --backdrop: #cde0f4;
    --sign-white: #ffffff;
    --brand-blue: #1f5cac;
    --slate-grey: #77787b;
  }
  html, body {
    margin: 0;
    padding: 0;
    width: 1200px;
    height: 1200px;
    overflow: hidden;
    background: var(--backdrop);
  }
  .canvas {
    position: relative;
    width: 1200px;
    height: 1200px;
  }
  .sign {
    position: absolute;
    left: 51px;
    top: 272px;
    width: 1098px;
    height: 656px;
    background: var(--sign-white);
  }
  .sign__rule {
    position: absolute;
    left: 0;
    width: 100%;
    height: 12px;
    background: var(--brand-blue);
  }
  .sign__rule--top { top: 0; }
  .sign__rule--bottom { bottom: 0; }
  .brand {
    position: absolute;
    left: 0;
    width: 100%;
    text-align: center;
    font-family: "Montserrat", sans-serif;
    font-weight: 700;
    color: var(--slate-grey);
    line-height: 1;
    margin: 0;
  }
  .brand__name {
    top: 140px;
    font-size: 150px;
    letter-spacing: 2px;
  }
  .brand__tagline {
    top: 338px;
    font-size: 112px;
    letter-spacing: 1px;
  }
  .phone-band {
    position: absolute;
    left: 0;
    top: 466px;
    width: 100%;
    height: 118px;
    background: var(--brand-blue);
    display: flex;
    align-items: center;
    justify-content: center;
  }
  .phone-band__number {
    font-family: "Montserrat", sans-serif;
    font-weight: 700;
    font-size: 118px;
    color: var(--sign-white);
    letter-spacing: 1px;
    line-height: 1;
  }
  .website {
    position: absolute;
    left: 0;
    top: 584px;
    width: 100%;
    height: 60px;
    display: flex;
    align-items: center;
    justify-content: center;
    font-family: "Open Sans", sans-serif;
    font-weight: 400;
    font-size: 42px;
    color: var(--brand-blue);
  }
</style>
</head>
<body>
<main class="canvas">
  <section class="sign" aria-label="Brookfell Self Storage road sign">
    <div class="sign__rule sign__rule--top"></div>
    <h1 class="brand brand__name">BROOKFELL</h1>
    <p class="brand brand__tagline">SELF STORAGE</p>
    <div class="phone-band">
      <span class="phone-band__number">478-216-4387</span>
    </div>
    <div class="website">www.BrookfellStorage.net</div>
    <div class="sign__rule sign__rule--bottom"></div>
  </section>
</main>
</body>
</html>
```